Cigar Ring Design

we are working on a project, which is an eCommerce store for cigars, now instead of selling all kind of existing brands this project is based on a BrassMeadowHouse concept where an outlet is linked to an actual Cigar factory,
so the cigar lines sold will come out under a BMH (BrassMeadowHouse) brand consisting of various labels, (think Barney Kettle, Harbor Crest, Willow Crest etc) I had an idea for the Cigar Rings for this project, where I put BM in an O (circle) of which I made mock ups (see attachement), now I am not a designer, I am sure a real designer can come up with something more stylish and unique.

```html
<!DOCTYPE html>
<html lang="en">
<head>
<meta charset="utf-8">
<title>BrassMeadowHouse Cigar Rings</title>
<link rel="stylesheet" href="https://fonts.googleapis.com/css2?family=Montserrat:wght@800&display=swap">
<style>
  :root {
    --paper: #ffffff;
    --wine: #9b1d22;
    --wine-deep: #6c1418;
    --ink: #000000;
    --ink-soft: #0d0d0d;
    --name-text: #ffffff;
  }
  html, body {
    margin: 0;
    padding: 0;
    overflow: hidden;
    background: var(--paper);
  }
  .canvas {
    position: relative;
    width: 1200px;
    height: 1088px;
    background: var(--paper);
    overflow: hidden;
  }
  .ring-band {
    position: absolute;
    left: 14px;
    width: 1172px;
  }
  .ring-band--wine { top: 30px; }
  .ring-band--black { top: 595px; }

  .ring-band__stripe,
  .ring-band__body {
    position: absolute;
    left: 0;
    width: 100%;
  }
  .ring-band__stripe--top { top: 0; height: 8px; }
  .ring-band__body {
    top: 38px;
    height: 385px;
    display: flex;
    align-items: center;
    justify-content: center;
  }
  .ring-band__stripe--bottom { top: 453px; height: 18px; }

  .ring-band--wine .ring-band__stripe {
    background: linear-gradient(90deg, var(--wine) 0%, var(--wine) 35%, var(--wine-deep) 60%, var(--wine) 85%);
  }
  .ring-band--wine .ring-band__body {
    background: linear-gradient(120deg, var(--wine) 0%, var(--wine) 30%, var(--wine-deep) 45%, var(--wine) 56%, var(--wine-deep) 70%, var(--wine) 85%);
  }
  .ring-band--black .ring-band__stripe { background: var(--ink); }
  .ring-band--black .ring-band__body {
    background: linear-gradient(120deg, var(--ink) 0%, var(--ink) 55%, var(--ink-soft) 75%, var(--ink) 100%);
  }

  .brand-name {
    margin: 0;
    font-family: "Montserrat", sans-serif;
    font-weight: 800;
    font-size: 150px;
    line-height: 1;
    letter-spacing: -3px;
    color: var(--name-text);
  }
</style>
</head>
<body>
<main class="canvas">
  <section class="ring-band ring-band--wine" aria-label="BrassMeadowHouse cigar ring, wine edition">
    <div class="ring-band__stripe ring-band__stripe--top"></div>
    <div class="ring-band__body">
      <p class="brand-name">BM</p>
    </div>
    <div class="ring-band__stripe ring-band__stripe--bottom"></div>
  </section>

  <section class="ring-band ring-band--black" aria-label="BrassMeadowHouse cigar ring, black edition">
    <div class="ring-band__stripe ring-band__stripe--top"></div>
    <div class="ring-band__body">
      <p class="brand-name">BM</p>
    </div>
    <div class="ring-band__stripe ring-band__stripe--bottom"></div>
  </section>
</main>
</body>
</html>
```